Tidewell Homecare

I am looking to have a website designed for a housekeeping company that looks similar to this one. https://marlowsnestcare.example/

I need 5 websites designed but will start with this one to see how I like it.

Industry/Entity Type

House Cleaning

Coding

Coded - Design and coding required

Number of Pages Required

5+ page

Font styles to use
Serif
Script

Colors
ffffff
fdf9cf
fbf289
fbee3f
d6edf3
86cae7
33a6d7
edf1f8
cedeed

```html
<!DOCTYPE html>
<html lang="en">
<head>
<meta charset="utf-8">
<title>Tidewell Homecare</title>
<link href="https://fonts.googleapis.com/css2?family=Mulish:wght@400;500;600;700&display=swap" rel="stylesheet">
<style>
:root{
  --white:#ffffff;
  --cream:#fdf9cf;
  --yellow:#fbee3f;
  --sky:#33a6d7;
  --sky-soft:#86cae7;
  --mist:#edf1f8;
  --ice:#cedeed;
  --ink:#222222;
  --text:#444444;
  --navy:#1d1f2b;
  --foot:#1e1f24;
}
*{box-sizing:border-box;margin:0;padding:0}
html,body{width:1200px;height:3583px;overflow:hidden}
body{font-family:"Mulish",sans-serif;color:var(--text);background:var(--white);position:relative}
.abs{position:absolute}
.btn{position:absolute;background:var(--yellow);color:var(--ink);font-size:12px;font-weight:700;text-transform:uppercase;display:flex;align-items:center;justify-content:center;letter-spacing:.3px}
.ph{position:absolute}
/* header */
.brand{left:143px;top:22px;display:flex;align-items:center;gap:12px;font-size:25px;font-weight:600;color:#3a3a3a}
.brand-mark{width:36px;height:36px;border-radius:50%;background:var(--sky-soft)}
.phone{left:755px;top:30px;font-size:22px;font-weight:600;color:var(--ink);display:flex;align-items:center;gap:8px}
.nav{left:0;top:88px;width:1200px;height:40px;background:var(--yellow);font-size:14px;font-weight:500;text-transform:uppercase;color:#555}
.nav span{position:absolute;top:11px}
.nav .on{color:var(--ink);font-weight:700}
/* hero */
.hero{left:0;top:128px;width:1200px;height:548px;
  background:
    linear-gradient(90deg,rgba(0,0,0,0) 64%,rgba(206,200,190,.85) 72%,rgba(176,170,160,.95) 100%),
    radial-gradient(ellipse 260px 120px at 90px 330px,rgba(70,110,60,.85),rgba(70,110,60,0)),
    linear-gradient(180deg,#a9cbe8 0%,#d6e6f2 28%,#eef3f6 44%,#2b8cbf 48%,#3c9ccb 58%,#74b6d8 66%,#5d9fc9 80%,#7fb4d6 100%)}
.hero-deck{left:620px;top:460px;width:580px;height:220px;background:linear-gradient(180deg,rgba(150,160,172,.0),rgba(140,148,160,.75) 40%,rgba(160,165,172,.85))}
.hero-title{left:0;top:298px;width:1200px;text-align:center;font-size:34px;font-weight:500;line-height:43px;color:#1a1a1a;text-transform:uppercase}
.arrow{position:absolute;width:44px;height:44px;border-radius:50%;background:#2a2a2a;display:flex;align-items:center;justify-content:center}
/* welcome */
.h2{font-size:33px;font-weight:600;color:var(--sky);line-height:43px}
.welcome-text{left:143px;top:866px;width:445px;font-size:16px;line-height:32px;color:#444}
.welcome-photo{left:644px;top:759px;width:411px;height:410px;
  background:
    radial-gradient(ellipse 90px 70px at 250px 150px,rgba(232,140,160,.9),rgba(232,140,160,0)),
    radial-gradient(ellipse 90px 70px at 340px 300px,rgba(232,130,150,.9),rgba(232,130,150,0)),
    radial-gradient(ellipse 70px 110px at 150px 230px,rgba(245,245,245,.95),rgba(245,245,245,0)),
    linear-gradient(180deg,#5c5048 0%,#8a7c70 30%,#cfc8bf 62%,#eeeae4 100%)}
/* services */
.services{left:0;top:1251px;width:1200px;height:506px;
  background:radial-gradient(ellipse 500px 180px at 600px 250px,rgba(80,86,100,.45),rgba(0,0,0,0)),linear-gradient(180deg,#232634,#1a1c27)}
.svc{position:absolute;top:1395px;width:290px;text-align:center;color:var(--white)}
.svc svg{display:block;margin:0 auto}
.svc .bar{width:160px;height:3px;background:var(--yellow);margin:30px auto 22px}
.svc h3{font-size:25px;font-weight:500}
.svc p{font-size:11px;line-height:19px;margin-top:10px;color:#ddd}
.svc .outline{width:120px;height:39px;border:1px solid #ccc;margin:16px auto 0;font-size:12px;font-weight:700;display:flex;align-items:center;justify-content:center}
/* testimonials */
.quote{left:643px;top:1940px;width:420px;font-size:17px;line-height:34px;color:#444}
.mini{position:absolute;width:22px;height:22px;border:1px solid #333;display:flex;align-items:center;justify-content:center}
.portrait{position:absolute;border-radius:50%;border:3px solid #fff;box-shadow:0 3px 10px rgba(0,0,0,.2)}
/* blog */
.blog{left:0;top:2337px;width:1200px;height:613px;
  background:linear-gradient(90deg,rgba(205,214,230,.7),rgba(236,240,247,.2) 30%,rgba(236,240,247,.2) 70%,rgba(205,214,230,.7)),linear-gradient(180deg,#e8edf6,#dde4ef 70%,#cfd7e4)}
.card{position:absolute;background:var(--white);padding:18px 20px;width:388px;height:141px}
.card .date{font-size:12px;font-weight:700;color:var(--sky)}
.card p{font-size:15px;line-height:27px;margin-top:8px;color:#444}
/* quote form */
.field{position:absolute;border:1px solid #bbb;font-size:11px;color:#444;padding:12px 14px;background:var(--white)}
/* footer */
.footer{left:0;top:3485px;width:1200px;height:98px;background:var(--foot);font-size:11px;color:#9a9a9a}
</style>
</head>
<body>

<header>
  <div class="abs brand"><span class="brand-mark"></span>Tidewell Homecare</div>
  <div class="abs phone">
    <svg width="18" height="18" viewBox="0 0 24 24"><path fill="#222" d="M6.6 10.8a15 15 0 0 0 6.6 6.6l2.2-2.2c.3-.3.7-.4 1-.2 1.1.4 2.3.6 3.6.6.6 0 1 .4 1 1V20c0 .6-.4 1-1 1C10.6 21 3 13.4 3 4c0-.6.4-1 1-1h3.5c.6 0 1 .4 1 1 0 1.3.2 2.5.6 3.6.1.3 0 .7-.2 1z"/></svg>
    555 010 4827
  </div>
  <div class="btn" style="left:935px;top:25px;width:120px;height:39px">Get a Quote</div>
  <nav class="abs nav">
    <span class="on" style="left:170px">Services</span>
    <span style="left:307px">Works</span>
    <span style="left:429px">Gift Cards</span>
    <span style="left:583px">Blog</span>
    <span style="left:690px">FAQs</span>
    <span style="left:796px">About Us</span>
    <span style="left:938px">Contact Us</span>
  </nav>
</header>

<section>
  <div class="ph hero" role="img" aria-label="Seaside villa with infinity pool and loungers overlooking the ocean"></div>
  <div class="ph hero-deck" aria-hidden="true"></div>
  <svg class="abs" style="left:0;top:600px" width="1200" height="80" viewBox="0 0 1200 80">
    <path d="M0 76 C200 60 300 20 520 40 C720 58 820 72 1000 50 C1100 36 1160 24 1200 20 L1200 80 L0 80Z" fill="#fff"/>
    <path d="M0 76 C200 60 300 20 520 40 C720 58 820 72 1000 50 C1100 36 1160 24 1200 20" fill="none" stroke="#2d8fc4" stroke-width="5"/>
  </svg>
  <h1 class="abs hero-title">Vestibulum Condimentum<br>Posuere Cursus</h1>
  <div class="btn" style="left:540px;top:393px;width:120px;height:40px">Get a Quote</div>
  <div class="arrow" style="left:54px;top:348px"><svg width="16" height="16" viewBox="0 0 16 16"><path d="M11 2 5 8l6 6" fill="none" stroke="#fff" stroke-width="2.5"/></svg></div>
  <div class="arrow" style="left:1099px;top:348px"><svg width="16" height="16" viewBox="0 0 16 16"><path d="M5 2l6 6-6 6" fill="none" stroke="#fff" stroke-width="2.5"/></svg></div>
</section>

<section>
  <div class="abs" style="left:888px;top:928px;width:450px;height:450px;border-radius:50%;background:var(--cream)"></div>
  <div class="abs" style="left:0;top:1251px;width:1200px;height:200px;background:var(--white)"></div>
  <h2 class="abs h2" style="left:143px;top:766px">Welcome to<br>Tidewell Homecare</h2>
  <p class="abs welcome-text">Proin placerat dapibus gravida. In tristique tristique nulla eget hendrerit. Maecenas vel tortor accumsan quam varius imperdiet vel eget elit. Aenean facilisis tincidunt lectus, id dictum nisi luctus eget. Vivamus efficitur ex condimentum, malesuada eros eget, feugiat nibh. Sed tellus ex, imperdiet eget gravida sit amet, volutpat eget turpis. In nec ultricies est. Etiam mattis augue vehicula odio posuere.</p>
  <div class="btn" style="left:143px;top:1113px;width:120px;height:40px">Read More</div>
  <div class="ph welcome-photo" role="img" aria-label="Cleaner in pink gloves spraying and wiping a white shag rug"></div>
</section>

<section>
  <div class="abs services" role="img" aria-label="Dark modern living room backdrop"></div>
  <h2 class="abs" style="left:0;top:1322px;width:1200px;text-align:center;font-size:32px;font-weight:600;color:var(--yellow)">Services</h2>
  <div class="svc" style="left:137px">
    <svg width="84" height="82" viewBox="0 0 84 82" fill="none" stroke="#fff" stroke-width="2.5"><rect x="8" y="4" width="30" height="22"/><path d="M23 26v8M16 34h14"/><rect x="56" y="2" width="20" height="78"/><path d="M60 12h12M60 22h12"/><path d="M2 40h74M6 40v40M56 58H6"/><rect x="36" y="48" width="14" height="8"/></svg>
    <div class="bar"></div><h3>Furniture Cleaning</h3>
    <p>Aenean placerat, nibh vel accumsan aliquet, magna nibh accumsan nibh, ac tempus nunc ipsum ac tellus. Cras augue magna, placerat eget.</p>
    <div class="outline">READ MORE</div>
  </div>
  <div class="svc" style="left:455px">
    <svg width="84" height="82" viewBox="0 0 84 82" fill="none" stroke="#fff" stroke-width="2.5"><rect x="2" y="2" width="20" height="16"/><rect x="30" y="2" width="20" height="16"/><rect x="58" y="2" width="22" height="16"/><path d="M6 26h12M6 32h12"/><path d="M70 28v10"/><rect x="2" y="40" width="80" height="40"/><rect x="24" y="50" width="36" height="24"/><path d="M30 44h4M40 44h4M50 44h4"/></svg>
    <div class="bar"></div><h3>Kitchen Cleaning</h3>
    <p>Aenean placerat, nibh vel accumsan aliquet, magna nibh accumsan nibh, ac tempus nunc ipsum ac tellus. Cras augue magna, placerat eget.</p>
    <div class="outline">READ MORE</div>
  </div>
  <div class="svc" style="left:771px">
    <svg width="84" height="82" viewBox="0 0 84 82" fill="none" stroke="#fff" stroke-width="2.5"><path d="M6 4h40M10 4v44M16 4v44M22 4v44M28 4v44M34 4v44M40 4v44"/><rect x="58" y="8" width="16" height="26" rx="3"/><path d="M62 16h8M62 22h8"/><path d="M2 48h80v10a14 14 0 0 1-14 14H16A14 14 0 0 1 2 58z"/><path d="M16 72l-4 8M68 72l4 8"/></svg>
    <div class="bar"></div><h3>Bathroom Cleaning</h3>
    <p>Aenean placerat, nibh vel accumsan aliquet, magna nibh accumsan nibh, ac tempus nunc ipsum ac tellus. Cras augue magna, placerat eget.</p>
    <div class="outline">READ MORE</div>
  </div>
</section>

<section>
  <div class="abs" style="left:143px;top:1838px;width:410px;height:410px;border-radius:50%;background:radial-gradient(circle,#f6f6f6 60%,#e6e6e6)"></div>
  <div class="portrait" style="left:184px;top:1878px;width:330px;height:330px;border-width:4px;background:radial-gradient(circle at 50% 48%,#f0d2bc 0%,#d9ad8c 32%,#9c7350 58%,#c7c2bc 82%,#e0ddd9 100%)" role="img" aria-label="Portrait of a smiling client"></div>
  <div class="portrait" style="left:148px;top:1866px;width:96px;height:96px;background:radial-gradient(circle at 50% 50%,#e2b998 0%,#c49474 40%,#6b5444 62%,#c9c4be 85%)" role="img" aria-label="Portrait of a client"></div>
  <div class="portrait" style="left:500px;top:1941px;width:68px;height:68px;background:radial-gradient(circle at 50% 50%,#c79a78 0%,#9b7054 45%,#3d3a38 70%,#d6d4d2 90%)" role="img" aria-label="Portrait of a client"></div>
  <div class="portrait" style="left:174px;top:2130px;width:52px;height:52px;background:radial-gradient(circle at 50% 50%,#ecc9ae 0%,#c79b7a 45%,#8a6a52 70%,#e4e1de 90%)" role="img" aria-label="Portrait of a client"></div>
  <div class="portrait" style="left:434px;top:2112px;width:118px;height:118px;background:radial-gradient(circle at 50% 50%,#f1cfb4 0%,#dcaa84 35%,#c9a064 60%,#9a8a7a 85%)" role="img" aria-label="Portrait of a client"></div>
  <h2 class="abs h2" style="left:643px;top:1883px">Testimonials</h2>
  <p class="abs quote">“ Quisque aliquet ex nec est vestibulum pulvinar. Pellentesque convallis molestie enim amet efficitur. Etiam imperdiet lectus. Vivamus lacus ultrices nec erat in, euismod iaculis mauris. Etiam vel massa elementum, bibendum tellus. ”</p>
  <div class="abs" style="left:643px;top:2116px;font-size:20px;color:var(--sky)">- Dana Reyes, City</div>
  <div class="mini" style="left:643px;top:2170px"><svg width="8" height="10"><path d="M6 1 2 5l4 4" fill="none" stroke="#333" stroke-width="1.5"/></svg></div>
  <div class="mini" style="left:672px;top:2170px"><svg width="8" height="10"><path d="M2 1l4 4-4 4" fill="none" stroke="#333" stroke-width="1.5"/></svg></div>
</section>

<section>
  <div class="abs blog" role="img" aria-label="Faded bright kitchen interior backdrop"></div>
  <h2 class="abs h2" style="left:0;top:2412px;width:1200px;text-align:center">Blog</h2>
  <svg class="abs" style="left:52px;top:2604px" width="22" height="32"><path d="M18 3 5 16l13 13" fill="none" stroke="#444" stroke-width="4"/></svg>
  <svg class="abs" style="left:1124px;top:2604px" width="22" height="32"><path d="M4 3l13 13L4 29" fill="none" stroke="#444" stroke-width="4"/></svg>
  <div class="ph" style="left:144px;top:2477px;width:420px;height:288px;background:
    radial-gradient(ellipse 70px 50px at 280px 90px,rgba(240,190,40,.9),rgba(240,190,40,0)),
    radial-gradient(ellipse 60px 80px at 50px 50px,rgba(90,140,60,.8),rgba(90,140,60,0)),
    radial-gradient(ellipse 80px 50px at 370px 20px,rgba(40,90,170,.8),rgba(40,90,170,0)),
    linear-gradient(180deg,#f2f0eb 0%,#ece6dd 22%,#c9a583 45%,#b8906c 70%,#a47d5d 100%)" role="img" aria-label="Cleaner vacuuming a beige sofa with yellow gloves"></div>
  <div class="card" style="left:160px;top:2725px"><div class="date">11 APRIL, 2020</div><p>Nunc sit amet consequat risus. Curabitur ac elit leo eleifend dui tellus in scelerisque elit porttitor massa.</p></div>
  <div class="ph" style="left:635px;top:2477px;width:420px;height:288px;background:
    radial-gradient(ellipse 80px 40px at 180px 200px,rgba(40,40,45,.8),rgba(40,40,45,0)),
    radial-gradient(ellipse 60px 90px at 110px 60px,rgba(40,70,150,.85),rgba(40,70,150,0)),
    linear-gradient(90deg,rgba(0,0,0,0) 55%,rgba(190,160,130,.6) 75%,rgba(220,220,220,.5) 100%),
    linear-gradient(180deg,#b9ada0 0%,#a89c90 35%,#8790a6 55%,#6d7893 80%,#5f6a86 100%)" role="img" aria-label="Carpet being cleaned with a steam extractor"></div>
  <div class="card" style="left:651px;top:2725px"><div class="date">11 APRIL, 2020</div><p>Nunc eu ligula sed quam pulvinar maximus in vitae eros. Proin porta fermentum ipsum, vel porttitor turpis venenatis luctus.</p></div>
</section>

<section>
  <h2 class="abs h2" style="left:0;top:3023px;width:1200px;text-align:center">Get a Quote</h2>
  <div class="field" style="left:394px;top:3087px;width:199px;height:39px">Name</div>
  <div class="field" style="left:607px;top:3087px;width:199px;height:39px">Email</div>
  <div class="field" style="left:394px;top:3143px;width:199px;height:39px">Phone</div>
  <div class="field" style="left:607px;top:3143px;width:199px;height:39px">Address</div>
  <div class="field" style="left:394px;top:3199px;width:412px;height:136px">Message</div>
  <div class="btn" style="left:540px;top:3360px;width:120px;height:38px;font-size:14px">Submit</div>
</section>

<footer class="abs footer">
  <div class="abs" style="left:144px;top:28px">Services &nbsp;&nbsp;|&nbsp;&nbsp; Works &nbsp;&nbsp;|&nbsp;&nbsp; Gift Cards &nbsp;&nbsp;|&nbsp;&nbsp; Blog &nbsp;&nbsp;|&nbsp;&nbsp; FAQs &nbsp;&nbsp;|&nbsp;&nbsp; About us &nbsp;&nbsp;|&nbsp;&nbsp; Contact Us</div>
  <div class="abs" style="left:144px;top:61px">Copyright © 2020 &nbsp;Tidewell Homecare. &nbsp;All rights reserved.</div>
  <div class="abs" style="left:993px;top:40px;width:18px;height:18px;border-radius:50%;background:#8a8a8a"></div>
  <div class="abs" style="left:1035px;top:40px;width:18px;height:18px;border-radius:50%;background:#8a8a8a"></div>
</footer>

</body>
</html>
```